Manufacturing company needs new business card.

I need a unique Business Card that will truly stand out. Nothing too busy. Simple is good, right? Not looking for a standard design either. No cookie cutter layout. I am just looking for something interesting and a bit different. Does't have to completely off the wall crazy, just not your run of the mill business card. Clean and modern with a touch of industrial.

Target Market(s)

Air conditioning industry, Architects, builders.

Industry/Entity Type

Business

Contact Information for Business Card

Details to be included on card are:

Peter Vance
Managing Director

T: 1300 847 519
M: 0428 593 174
W: www.brenvaleworks.com.au
E: peter.vance@brenvaleworks.com.au
A: 58 Harwick Lane, Sydney NSW 2000

Font styles to use
Sans Serif

Colors
0355a3
848484
fbfbfb

Requirements
Must have
• Card design must be landscape.

```html
<!DOCTYPE html>
<html lang="en">
<head>
<meta charset="utf-8">
<title>Brenvale Works – Business Card</title>
<link href="https://fonts.googleapis.com/css2?family=Open+Sans:wght@400;600;700&display=swap" rel="stylesheet">
<style>
  :root {
    --brand-blue: #0355a3;
    --brand-grey: #848484;
    --brand-white: #fbfbfb;
    --page-bg: #e6e6e6;
    --silver-light: #d8d8d8;
    --silver-mid: #b9b9b9;
    --silver-dark: #8f8f8f;
  }
  * { box-sizing: border-box; margin: 0; padding: 0; }
  html, body { width: 1200px; height: 894px; overflow: hidden; }
  body {
    background: var(--page-bg);
    font-family: "Open Sans", Arial, sans-serif;
    display: flex;
    flex-direction: column;
    align-items: center;
    justify-content: center;
    gap: 56px;
  }
  .card {
    position: relative;
    width: 620px;
    height: 354px;
    border-radius: 22px;
    overflow: hidden;
    background: linear-gradient(170deg, var(--silver-light) 0%, #cbcbcb 35%, var(--silver-mid) 70%, var(--silver-dark) 100%);
    box-shadow: 0 10px 28px rgba(0,0,0,0.18);
  }
  .brand {
    position: absolute;
    top: 38px;
    left: 42px;
    display: flex;
    align-items: center;
    gap: 16px;
  }
  .brand-square {
    width: 58px;
    height: 58px;
    border-radius: 6px;
    background: var(--brand-blue);
  }
  .brand-name {
    font-weight: 600;
    font-size: 42px;
    color: var(--brand-blue);
    letter-spacing: -0.5px;
  }
  .brand-rule {
    position: absolute;
    top: 118px;
    left: 42px;
    width: 280px;
    height: 2px;
    background: var(--brand-grey);
  }
  /* contact side */
  .contact-list {
    position: absolute;
    left: 110px;
    top: 150px;
    list-style: none;
    font-size: 20px;
    line-height: 33px;
    color: var(--brand-white);
  }
  .contact-list .label {
    display: inline-block;
    width: 30px;
    color: var(--brand-blue);
  }
  /* name side */
  .person {
    position: absolute;
    left: 42px;
    top: 190px;
  }
  .person-name {
    font-weight: 700;
    font-size: 50px;
    color: var(--brand-white);
    letter-spacing: 0.5px;
    line-height: 1.1;
  }
  .person-title {
    font-size: 27px;
    color: var(--brand-blue);
    letter-spacing: 1.2px;
  }
  .accent-panel {
    position: absolute;
    right: 0;
    top: 150px;
    width: 250px;
    height: 204px;
    border-top-left-radius: 18px;
    background: rgba(255,255,255,0.14);
  }
</style>
</head>
<body>
  <section class="card card-contact" aria-label="Card back with contact details">
    <div class="brand">
      <span class="brand-square"></span>
      <span class="brand-name">Brenvale Works</span>
    </div>
    <div class="brand-rule"></div>
    <ul class="contact-list">
      <li><span class="label">t:</span>1300 847 519</li>
      <li><span class="label">m:</span>0428 593 174</li>
      <li><span class="label">e:</span>peter.vance@brenvaleworks.com.au</li>
      <li><span class="label">a:</span>58 Harwick Lane, Sydney NSW 2000</li>
      <li><span class="label">w:</span>www.brenvaleworks.com.au</li>
    </ul>
  </section>

  <section class="card card-name" aria-label="Card front with name and title">
    <div class="accent-panel"></div>
    <div class="brand">
      <span class="brand-square"></span>
      <span class="brand-name">Brenvale Works</span>
    </div>
    <div class="brand-rule"></div>
    <div class="person">
      <p class="person-name">Peter Vance</p>
      <p class="person-title">Managing Director</p>
    </div>
  </section>
</body>
</html>
```